Homes, Invest in Non-performing loans

We need only 3 web pages, one for the home, one for the content, one for the properties.
The main focus of our business is to offer non performing loans (before foreclosures) to the general public. All the non-performing mortgages will end in a house, an apartment, a store, etc.
Our customers are able to invest from 10,000usd to 1,000,000usd (average 50,000usd).
Our customers' usual focus groups are employees who want second earnings, perceiving the business feeling without outlay time. They look for a solid finance sense corporation that confers them certainty.
Nearly all our clients desire the house, apartment, store, etc. more than the actual earnings.
The name of our company is BRIXEL
Reason: We value the time and effort you already invest in our project. We realize that we did't come back on some of the doubts requested by the designers. It will be inequitable to the designers who prerequisite our feedback. We also appreciate the comprehension of the community in this postponement.
Reason: Designers,
We really apreciate all the time and effort you put on our project. From the begining we ask for 3 pages, so now we will leave the 10 finalist and provide some extra time to submit the other 2 pages.
We will race the price in 10%
Target Market(s)
Our customers average investors works as employees and want to have a second income or business without spending time. (People from 35 to 50)
Industry/Entity Type
Finance
Requirements
Should not have
- FLASH

```html
<!DOCTYPE html>
<html lang="en">
<head>
<meta charset="utf-8">
<title>BRIXEL — Invest in Non-performing Loans</title>
<link href="https://fonts.googleapis.com/css2?family=Open+Sans:ital,wght@0,400;0,600;0,700;0,800;1,400&family=Titillium+Web:ital,wght@1,700&family=Anton&family=Arimo&display=swap" rel="stylesheet">
<style>
:root{
  --olive:#7c7a20;
  --olive-dark:#66651a;
  --olive-light:#a6a830;
  --green:#8bb13a;
  --green-dark:#6f8f1e;
  --ink:#2b2b2b;
  --text:#555;
  --bg:#ececec;
  --frame:#c4c4c4;
  --footer:#cdcdcd;
  --red:#7a0b0b;
}
*{box-sizing:border-box;margin:0;padding:0}
html,body{width:1200px;height:1117px;overflow:hidden}
body{position:relative;background:var(--bg);font-family:"Open Sans",sans-serif;color:var(--text)}
.abs{position:absolute}
.topline{left:0;top:0;width:1200px;height:6px;background:var(--olive)}
.header{left:0;top:6px;width:1200px;height:126px;background:#fff}
.brand{left:174px;top:40px;display:flex;align-items:center;gap:8px;font-weight:800;font-size:34px;color:var(--ink);letter-spacing:1px}
.brand .mark{width:22px;height:22px;background:var(--olive-light)}
.search{left:809px;top:15px;width:214px;height:32px;border:3px solid #d6d6d6;border-radius:6px;background:linear-gradient(#fff,#ececec);font-size:11px;color:#888;padding:6px 8px}
.search .go{position:absolute;right:-3px;top:-3px;width:34px;height:32px;background:linear-gradient(#444,#111);border-radius:5px}
.search .go svg{position:absolute;left:11px;top:8px}
.btn{top:77px;height:20px;border-radius:10px;background:linear-gradient(#bcd45a,#8eac2a);font-size:12px;color:#1e2a05;text-align:center;line-height:20px;box-shadow:2px 2px 3px #bbb}
.social{top:74px;width:30px;height:30px;border-radius:50%;background:radial-gradient(circle at 40% 35%,#5bb9e6,#1a6fa6)}
.hero{left:0;top:132px;width:1200px;height:285px;background:var(--olive)}
.hero .glow{left:240px;top:40px;width:800px;height:230px;background:radial-gradient(ellipse at 80% 40%,rgba(230,235,120,.55),rgba(124,122,32,0) 65%)}
.hero .strip{left:0;top:270px;width:1200px;height:15px;background:var(--olive-dark)}
.hero .person{left:156px;top:42px;width:264px;height:228px;background:linear-gradient(#c99b6a,#3a3330 45%,#2a2624);border-radius:100px 100px 0 0}
.hero .calc{left:768px;top:38px;width:268px;height:223px;background:linear-gradient(135deg,#d9c25a,#8c8c8c 50%,#e4e4e4);border-radius:30px;transform:rotate(14deg)}
.hero .panel{left:390px;top:60px;width:470px;height:118px;background:rgba(255,255,255,.15)}
.hero .line1{left:393px;top:70px;font-family:"Titillium Web",sans-serif;font-style:italic;font-weight:700;font-size:30px;color:#fff;text-shadow:1px 2px 3px rgba(0,0,0,.4)}
.hero .line2{left:390px;top:108px;font-family:"Anton",sans-serif;font-size:46px;color:#111;letter-spacing:1px;word-spacing:14px}
.hero .line2 .to{color:#fff;margin:0 6px}
.nav{left:162px;top:113px;width:876px;height:42px;background:linear-gradient(#3b3b3b,#0e0e0e);border-radius:4px;display:flex}
.nav a{color:#fff;text-decoration:none;font-weight:700;font-size:12px;display:flex;align-items:center;justify-content:center;border-right:1px solid #555}
.nav a:last-child{border:0}
.card{width:285px;height:138px;background:#fff;border:7px solid var(--frame)}
.card h3{margin:4px 4px 0;height:30px;padding-left:8px;background:linear-gradient(90deg,#6d6d6d,#9a9a9a 55%,#fff);color:#fff;font-size:15px;font-weight:700;line-height:30px}
.card p{margin:6px 6px 0 7px;font-size:10.3px;line-height:15.4px;color:#444}
.card .more{position:absolute;right:11px;bottom:8px;width:18px;height:18px;border-radius:50%;border:1px solid #aaa;background:#fff}
.card .more svg{position:absolute;left:6px;top:4px}
.featured{left:768px;top:437px;width:264px;height:300px;background:var(--olive);border-radius:4px;overflow:hidden}
.featured h2{height:36px;background:linear-gradient(#1c1c1c,#000);color:#fff;font-size:14.5px;font-weight:700;padding:10px 12px}
.note{position:absolute;left:9px;width:240px;height:82px}
.note .photo{position:absolute;left:0;top:0;width:88px;height:70px;background:linear-gradient(#9cb6cf,#8a8a8a 55%,#6c8a3a);border:2px solid #ddd}
.note .info{position:absolute;left:108px;top:0;font-size:10.2px;line-height:14.5px;color:#fff}
.note .info b{color:#111;font-weight:600}
.note .read{position:absolute;left:108px;top:56px;color:var(--red);font-size:10.5px;font-weight:700}
.note.sep{border-bottom:1px dashed #b2b06a}
.qs{left:160px;top:756px;width:873px;height:47px;background:linear-gradient(#a8c64c,#6c8c16);border-radius:3px;color:#fff;font-weight:700;font-size:16px;padding:14px 17px}
.form{left:159px;top:819px;width:250px;height:175px;background:#fff;border-radius:4px}
.field{position:absolute;left:14px;font-size:11.5px;font-style:italic;color:#333}
.field span{position:absolute;left:88px;top:-5px;width:148px;height:21px;background:#e0e0e0}
.form .login{position:absolute;left:90px;top:145px;width:65px;height:20px;background:var(--green-dark);border-radius:3px;color:#fff;font-style:italic;font-weight:700;font-size:14px;text-align:center;line-height:20px}
.sell{left:429px;top:818px;width:603px;height:33px;background:linear-gradient(90deg,rgba(255,255,255,0),#fff 15%,#fff 85%,rgba(255,255,255,0))}
.sell h2{text-align:center;font-weight:400;font-size:19px;color:#555;padding-top:5px}
.sell-text{left:436px;top:866px;width:440px;font-size:12.2px;line-height:16.2px;color:#555}
.sell-read{left:772px;top:969px;width:82px;height:18px;background:var(--green-dark);color:#fff;font-size:10.5px;text-align:center;line-height:18px}
.sell-brand{left:898px;top:878px;display:flex;align-items:center;gap:8px;font-weight:800;font-size:30px;color:var(--ink)}
.sell-brand .mark{width:18px;height:18px;background:var(--olive-light)}
.footer{left:0;top:1011px;width:1200px;height:106px;background:var(--footer);border-top:7px solid #bdbdbd;font-family:"Arimo",sans-serif;font-size:11px;color:#333}
.footer .links{position:absolute;top:25px;width:1200px;text-align:center;word-spacing:1px}
.footer .rule{position:absolute;left:140px;top:56px;width:880px;border-top:1px solid #dcdcdc}
.footer .copy{position:absolute;top:73px;width:1200px;text-align:center}
</style>
</head>
<body>
<div class="abs topline"></div>
<div class="abs header"></div>
<div class="abs brand"><span class="mark"></span>BRIXEL</div>
<div class="abs search">SEARCH :<span class="go"><svg width="12" height="16" viewBox="0 0 12 16"><path d="M2 1l7 7-7 7" stroke="#fff" stroke-width="2.5" fill="none"/></svg></span></div>
<div class="abs btn" style="left:719px;width:76px">Register</div>
<div class="abs btn" style="left:809px;width:76px">Login</div>
<div class="abs social" style="left:916px" aria-label="Professional network"></div>
<div class="abs social" style="left:955px" aria-label="Microblog"></div>
<div class="abs social" style="left:994px" aria-label="Social network"></div>

<section class="abs hero">
  <div class="abs glow"></div>
  <div class="abs panel"></div>
  <div class="abs person" role="img" aria-label="Smiling businesswoman in a pinstripe suit presenting with an open hand"></div>
  <div class="abs calc" role="img" aria-label="Model house sitting on a calculator"></div>
  <div class="abs line1">Our customers are able to invest</div>
  <div class="abs line2">10,000 <span class="to">TO</span> 1,000,000</div>
  <div class="abs strip"></div>
</section>

<nav class="abs nav">
  <a style="width:97px">HOME</a><a style="width:116px">ABOUT US</a><a style="width:117px">BUY NOTES</a><a style="width:127px">SALE NOTES</a><a style="width:197px">PRODUCTS DEFINATION</a><a style="width:86px">FAQ'S</a><a style="width:136px">CONTACT US</a>
</nav>

<article class="abs card" style="left:161px;top:437px"><h3>HEADING 1</h3><p>Lorem Ipsum is simply dummy text of the printing and typesetting industry. Lorem Ipsum has been the indus-try's standard dummy text ever since the</p><span class="more"><svg width="6" height="8"><path d="M0 0l6 4-6 4z" fill="#2b4fa8"/></svg></span></article>
<article class="abs card" style="left:465px;top:437px"><h3>HEADING 2</h3><p>Lorem Ipsum is simply dummy text of the printing and typesetting industry. Lorem Ipsum has been the indus-try's standard dummy text ever since the</p><span class="more"><svg width="6" height="8"><path d="M0 0l6 4-6 4z" fill="#2b4fa8"/></svg></span></article>
<article class="abs card" style="left:161px;top:600px"><h3>HEADING 3</h3><p>Lorem Ipsum is simply dummy text of the printing and typesetting industry. Lorem Ipsum has been the indus-try's standard dummy text ever since the</p><span class="more"><svg width="6" height="8"><path d="M0 0l6 4-6 4z" fill="#2b4fa8"/></svg></span></article>
<article class="abs card" style="left:465px;top:600px"><h3>HEADING 4</h3><p>Lorem Ipsum is simply dummy text of the printing and typesetting industry. Lorem Ipsum has been the indus-try's standard dummy text ever since the</p><span class="more"><svg width="6" height="8"><path d="M0 0l6 4-6 4z" fill="#2b4fa8"/></svg></span></article>

<aside class="abs featured">
  <h2>FEATURED NOTES</h2>
  <div class="note sep" style="top:44px"><div class="photo" role="img" aria-label="Two-storey house with lawn"></div><div class="info"><b>OMAHA, NE</b><br>UPB: $71,898.87<br>Note Rate: 12.200%</div><div class="read">» Readmore...</div></div>
  <div class="note sep" style="top:133px"><div class="photo" role="img" aria-label="Two-storey house with lawn"></div><div class="info"><b>OMAHA, NE</b><br>UPB: $71,898.87<br>Note Rate: 12.200%</div><div class="read">» Readmore...</div></div>
  <div class="note" style="top:224px"><div class="photo" role="img" aria-label="Two-storey house with lawn"></div><div class="info"><b>OMAHA, NE</b><br>UPB: $71,898.87<br>Note Rate: 12.200%</div><div class="read">» Readmore...</div></div>
</aside>

<div class="abs qs">NOTE QUICK SEARCH</div>
<form class="abs form">
  <div class="field" style="top:22px">Product ID<span></span></div>
  <div class="field" style="top:54px">Loan Status<span></span></div>
  <div class="field" style="top:86px">Lien Position<span></span></div>
  <div class="field" style="top:119px">State<span></span></div>
  <div class="login">Login</div>
</form>

<div class="abs sell"><h2>SELL Notes / BUY Notes</h2></div>
<p class="abs sell-text">Nation's Leading Note Trading Plataform<br>Hosted by Brixel Lender Services, Inc., the nation's leading private money services provider, BRIXEL EXCHANGE offers Buyers and Sellers a secure, easy to use internet trading platform that actually guides clients through every step of the Buy/Sell process.</p>
<div class="abs sell-read">» Readmore...</div>
<div class="abs sell-brand"><span class="mark"></span>BRIXEL</div>

<footer class="abs footer">
  <div class="links">About us &nbsp;| &nbsp;Advertise with Ratewise &nbsp;| &nbsp;Partners Press Room &nbsp;| &nbsp;Investor Relations &nbsp;| &nbsp;Free Content Center &nbsp;| &nbsp;Contact Us &nbsp;| &nbsp;Sitemap</div>
  <div class="rule"></div>
  <div class="copy">© 2012 All Rights Reserved. &nbsp; Privacy Policy/ Terms of Use</div>
</footer>
</body>
</html>
```